New Website Footer for a Supercar dealership.

I'm looking to get a newly designed footer created for our website www.velmorauto.com - one version for Desktop and 1 trimmed down version for mobile. We have one in place at the moment but I want to start it from scratch and create something far better. I know what I want to include and I have a rough design to work from which I have included in the uploaded files and I am just looking for someone to give it a high end luxury design.

If you see the sketch I've done - it must include the following links
- CURRENT STOCK
- SELL YOUR CAR
- PREVIOUSLY SOLD
Ideally use the same font that we have on our website in the top navigation

Secondary Links (in lower case)
- Delivery & Shipping
- Privacy Policy
- Modern Slavery Statement
- Luxury Cars
- Contact Us

I want also want to include
- Opening Hours
- Widget for Ratewise
- Widget for Quorra Ratings
- 4 images for awards we have won (I have included in uploaded files)
- Mailing List Sign Up
- Our company logo and address
- Brisk Finance logo (partner)
- Cookie Policy and Site Map links.
- Social Media icons

You do not have to stick to the layout of my design - feel free to change it about. I am open to colour but it needs to stay subtle and ideally working within Greyscale.

I am looking to have a black background but has a textured element to it. I was thinking along the lines of carbon fibre effect or even better would be a "Forged carbon fibre" effect in the background - I have included a screenshot of what ford carbon fibre looks like.

Target Market(s)

Luxury high end buyers

Industry/Entity Type

Automotive

Number of Pages Required

1 page

Font styles to use
Serif
Sans Serif

Colors

Designer to choose only greyscale colors for use in the design.

Requirements
Must have
• 1 Version for Desktop
1 Version for Mobile

```html
<!DOCTYPE html>
<html lang="en">
<head>
<meta charset="utf-8">
<title>Velmor Auto – Footer, Desktop and Mobile</title>
<link href="https://fonts.googleapis.com/css2?family=Cinzel:wght@500;600&family=Lato:wght@400&display=swap" rel="stylesheet">
<style>
  :root {
    --page: #ffffff;
    --carbon-a: #363636;
    --carbon-b: #262626;
    --carbon-c: #303030;
    --band: #161616;
    --wedge: #d9d9d9;
    --ink: #d4d4d4;
    --ink-bright: #f0f0f0;
    --ink-soft: #9a9a9a;
    --button-bg: #1d1d1d;
    --button-line: #7a7a7a;
    --input-line: #6a6a6a;
    --badge-dark: #151515;
    --badge-light: #f2f2f2;
    --badge-line: #cfcfcf;
    --serif: "Cinzel", "Times New Roman", serif;
    --sans: "Lato", "Helvetica Neue", Arial, sans-serif;
  }
  * { box-sizing: border-box; margin: 0; padding: 0; }
  html, body { width: 1043px; height: 1200px; overflow: hidden; background: var(--page); }
  body { position: relative; font-family: var(--sans); color: var(--ink); }

  .footer { position: absolute; }
  .footer--desktop { left: 44px; top: 60px; width: 676px; height: 476px; }
  .footer--mobile { left: 755px; top: 50px; width: 234px; height: 1108px; }

  .footer__wedge { position: absolute; left: 0; top: 0; width: 100%; height: 22px; }
  .footer__surface {
    position: absolute; inset: 0;
    background: linear-gradient(160deg, var(--carbon-a) 0%, var(--carbon-b) 45%, var(--carbon-c) 100%);
    clip-path: polygon(0 0, 100% 20px, 100% 100%, 0 100%);
  }
  .abs { position: absolute; }

  .nav-button {
    position: absolute; width: 171px; height: 24px;
    background: var(--button-bg); border: 1px solid var(--button-line);
    font-family: var(--serif); font-weight: 500; font-size: 8.5px; letter-spacing: 0.9px;
    color: var(--ink-bright); padding-left: 9px; line-height: 22px; text-transform: uppercase;
  }

  .heading {
    position: absolute; font-family: var(--serif); font-weight: 600;
    font-size: 11.5px; letter-spacing: 0.8px; color: var(--ink-bright); white-space: nowrap;
  }

  .link-list { position: absolute; list-style: none; font-size: 8.5px; line-height: 20px; }

  .hours { position: absolute; font-size: 8.5px; line-height: 22px; }
  .hours__row { display: flex; }
  .hours__day { width: 75px; }

  .copy { position: absolute; font-size: 8.5px; line-height: 13.5px; white-space: nowrap; }

  .badge { position: absolute; }
  .badge--dark { background: var(--badge-dark); }
  .badge--light { background: var(--badge-light); border: 1px solid var(--badge-line); }

  .rating { position: absolute; text-align: center; font-size: 9px; line-height: 11px; color: var(--ink-bright); white-space: nowrap; }

  .signup { position: absolute; height: 26px; display: flex; border: 1px solid var(--input-line); background: rgba(0,0,0,0.12); }
  .signup__field { flex: 1; font-size: 8.5px; line-height: 24px; padding-left: 8px; color: var(--ink); }
  .signup__button {
    width: 65px; background: #0e0e0e; font-family: var(--serif); font-weight: 600;
    font-size: 8px; letter-spacing: 0.8px; line-height: 24px; text-align: center; color: var(--ink-bright);
  }

  .brand { position: absolute; font-family: var(--serif); font-weight: 500; font-size: 22px; letter-spacing: 1px; color: var(--ink-bright); white-space: nowrap; }
  .partner { position: absolute; font-family: var(--sans); font-size: 15px; color: var(--ink-soft); white-space: nowrap; }

  .social-band { position: absolute; left: 0; width: 100%; background: var(--band); }
  .follow { position: absolute; font-family: var(--serif); font-weight: 600; font-size: 13px; letter-spacing: 1px; color: var(--ink-bright); white-space: nowrap; }
  .social { position: absolute; width: 80px; margin-left: -40px; text-align: center; }
  .social__name { font-family: var(--serif); font-weight: 600; font-size: 10px; letter-spacing: 0.8px; color: var(--ink-bright); line-height: 12px; }
  .social__mark { display: block; margin: 4px auto 0; }

  .legal { position: absolute; font-size: 7.5px; white-space: nowrap; color: var(--ink); }
</style>
</head>
<body>

<!-- Desktop footer -->
<footer class="footer footer--desktop">
  <div class="footer__surface"></div>
  <svg class="footer__wedge" viewBox="0 0 676 22" preserveAspectRatio="none" aria-hidden="true">
    <polygon points="300,9 676,0 676,20" fill="var(--wedge)"/>
  </svg>

  <div class="nav-button" style="left:42px; top:46px;">Current Stock</div>
  <div class="nav-button" style="left:42px; top:76px;">Sell Your Car</div>
  <div class="nav-button" style="left:42px; top:106px;">Previously Sold</div>

  <h3 class="heading" style="left:42px; top:144px;">Opening Hours</h3>
  <div class="hours" style="left:42px; top:164px;">
    <div class="hours__row"><span class="hours__day">Monday:</span><span>8:30am-6:00pm</span></div>
    <div class="hours__row"><span class="hours__day">Tuesday:</span><span>8:30am-6:00pm</span></div>
    <div class="hours__row"><span class="hours__day">Wednesday:</span><span>8:30am-6:00pm</span></div>
    <div class="hours__row"><span class="hours__day">Thursday:</span><span>8:30am-6:00pm</span></div>
    <div class="hours__row"><span class="hours__day">Friday:</span><span>8:30am-6:00pm</span></div>
    <div class="hours__row"><span class="hours__day">Saturday:</span><span>9:00am-5:00pm</span></div>
    <div class="hours__row"><span class="hours__day">Sunday:</span><span>By Appointment Only</span></div>
  </div>

  <h3 class="heading" style="left:259px; top:42px;">Quick Links</h3>
  <ul class="link-list" style="left:259px; top:61px;">
    <li>Delivery &amp; Shipping</li>
    <li>Privacy Policy</li>
    <li>Modern Slavery Statement</li>
    <li>Luxury Cars</li>
    <li>Contact Us</li>
  </ul>

  <div class="badge badge--dark" style="left:259px; top:176px; width:62px; height:57px;" role="img" aria-label="Award badge: companies to inspire listing"></div>
  <div class="badge badge--light" style="left:316px; top:176px; width:67px; height:57px;" role="img" aria-label="Award badge: independent dealer of the year"></div>
  <div class="badge badge--light" style="left:259px; top:240px; width:62px; height:34px;" role="img" aria-label="Award badge: fastest growing companies"></div>
  <div class="badge badge--light" style="left:316px; top:240px; width:67px; height:34px;" role="img" aria-label="Award badge: influential dealer on social media"></div>

  <div class="rating" style="left:259px; top:282px;">“Excellent”<br>Ratewise<br>★★★★★</div>
  <div class="rating" style="left:316px; top:288px; width:67px;">Quorra<br>Ratings ★★★★★</div>

  <h3 class="heading" style="left:441px; top:42px;">Sign Up Mailing List</h3>
  <p class="copy" style="left:441px; top:64px;">For event, invitation ,exclusive, previews<br>Lastest stock, + Special Offers</p>
  <div class="signup" style="left:441px; top:98px; width:193px;">
    <span class="signup__field">Enter Email</span>
    <span class="signup__button">Subscribe</span>
  </div>

  <div class="brand" style="left:441px; top:145px;">Velmor Auto</div>
  <p class="copy" style="left:441px; top:188px; line-height:14.5px;">Harrow Lane (B412), Elmsworth,<br>Surrey KT9 4QD</p>

  <h3 class="heading" style="left:441px; top:235px;">Partners</h3>
  <div class="partner" style="left:441px; top:266px;">Brisk Finance</div>
  <div class="partner" style="left:540px; top:266px;">Calder Bank</div>

  <p class="copy" style="left:441px; top:313px;">Cookie Policy &nbsp;/&nbsp; Site Map</p>

  <div class="social-band" style="top:353px; height:75px;">
    <div class="follow" style="left:42px; top:29px;">Follow Us:</div>
    <div class="social" style="left:184px; top:21px;"><div class="social__name">Faceline</div><svg class="social__mark" width="11" height="11" aria-hidden="true"><circle cx="5.5" cy="5.5" r="4.5" fill="none" stroke="var(--ink-bright)" stroke-width="1.2"/></svg></div>
    <div class="social" style="left:278px; top:21px;"><div class="social__name">Chatter</div><svg class="social__mark" width="11" height="11" aria-hidden="true"><circle cx="5.5" cy="5.5" r="4.5" fill="none" stroke="var(--ink-bright)" stroke-width="1.2"/></svg></div>
    <div class="social" style="left:374px; top:21px;"><div class="social__name">Picturo</div><svg class="social__mark" width="11" height="11" aria-hidden="true"><circle cx="5.5" cy="5.5" r="4.5" fill="none" stroke="var(--ink-bright)" stroke-width="1.2"/></svg></div>
    <div class="social" style="left:476px; top:21px;"><div class="social__name">Linkwork</div><svg class="social__mark" width="11" height="11" aria-hidden="true"><circle cx="5.5" cy="5.5" r="4.5" fill="none" stroke="var(--ink-bright)" stroke-width="1.2"/></svg></div>
    <div class="social" style="left:573px; top:21px;"><div class="social__name">Viewcast</div><svg class="social__mark" width="11" height="11" aria-hidden="true"><circle cx="5.5" cy="5.5" r="4.5" fill="none" stroke="var(--ink-bright)" stroke-width="1.2"/></svg></div>
  </div>

  <p class="legal" style="left:0; width:100%; text-align:center; top:447px;">Copyright © 2020. Company Name All Right Reserved</p>
</footer>

<!-- Mobile footer -->
<footer class="footer footer--mobile">
  <div class="footer__surface"></div>
  <svg class="footer__wedge" viewBox="0 0 234 22" preserveAspectRatio="none" aria-hidden="true">
    <polygon points="86,7 234,0 234,20" fill="var(--wedge)"/>
  </svg>

  <div class="nav-button" style="left:10px; top:42px;">Current Stock</div>
  <div class="nav-button" style="left:10px; top:72px;">Sell Your Car</div>
  <div class="nav-button" style="left:10px; top:101px;">Previously Sold</div>

  <h3 class="heading" style="left:10px; top:142px;">Quick Links</h3>
  <ul class="link-list" style="left:10px; top:160px;">
    <li>Delivery &amp; Shipping</li>
    <li>Privacy Policy</li>
    <li>Modern Slavery Statement</li>
    <li>Luxury Cars</li>
    <li>Contact Us</li>
  </ul>

  <h3 class="heading" style="left:10px; top:270px;">Opening Hours</h3>
  <div class="hours" style="left:10px; top:290px;">
    <div class="hours__row"><span class="hours__day">Monday:</span><span>8:30am-6:00pm</span></div>
    <div class="hours__row"><span class="hours__day">Tuesday:</span><span>8:30am-6:00pm</span></div>
    <div class="hours__row"><span class="hours__day">Wednesday:</span><span>8:30am-6:00pm</span></div>
    <div class="hours__row"><span class="hours__day">Thursday:</span><span>8:30am-6:00pm</span></div>
    <div class="hours__row"><span class="hours__day">Friday:</span><span>8:30am-6:00pm</span></div>
    <div class="hours__row"><span class="hours__day">Saturday:</span><span>9:00am-5:00pm</span></div>
    <div class="hours__row"><span class="hours__day">Sunday:</span><span>By Appointment Only</span></div>
  </div>

  <div class="badge badge--dark" style="left:10px; top:463px; width:62px; height:57px;" role="img" aria-label="Award badge: companies to inspire listing"></div>
  <div class="badge badge--light" style="left:84px; top:463px; width:67px; height:57px;" role="img" aria-label="Award badge: independent dealer of the year"></div>
  <div class="badge badge--light" style="left:10px; top:528px; width:62px; height:34px;" role="img" aria-label="Award badge: fastest growing companies"></div>
  <div class="badge badge--light" style="left:84px; top:528px; width:67px; height:34px;" role="img" aria-label="Award badge: influential dealer on social media"></div>

  <div class="rating" style="left:10px; top:569px;">“Excellent”<br>Ratewise<br>★★★★★</div>

  <h3 class="heading" style="left:11px; top:622px;">Partners</h3>
  <div class="partner" style="left:10px; top:655px;">Brisk Finance</div>
  <div class="partner" style="left:108px; top:655px;">Calder Bank</div>

  <h3 class="heading" style="left:10px; top:702px;">Sign Up Mailing List</h3>
  <p class="copy" style="left:10px; top:724px;">For event, invitation ,exclusive, previews<br>Lastest stock, + Special Offers</p>
  <div class="signup" style="left:10px; top:759px; width:193px;">
    <span class="signup__field">Enter Email</span>
    <span class="signup__button">Subscribe</span>
  </div>

  <div class="brand" style="left:10px; top:808px;">Velmor Auto</div>
  <p class="copy" style="left:11px; top:850px; line-height:14.5px;">Harrow Lane (B412), Elmsworth,<br>Surrey KT9 4QD</p>
  <p class="copy" style="left:11px; top:887px;">Cookie Policy &nbsp;/&nbsp; Site Map</p>

  <div class="social-band" style="top:917px; height:153px;">
    <div class="follow" style="left:0; width:100%; text-align:center; top:19px;">Follow Us:</div>
    <div class="social" style="left:40px; top:52px;"><div class="social__name">Faceline</div><svg class="social__mark" width="11" height="11" aria-hidden="true"><circle cx="5.5" cy="5.5" r="4.5" fill="none" stroke="var(--ink-bright)" stroke-width="1.2"/></svg></div>
    <div class="social" style="left:114px; top:52px;"><div class="social__name">Chatter</div><svg class="social__mark" width="11" height="11" aria-hidden="true"><circle cx="5.5" cy="5.5" r="4.5" fill="none" stroke="var(--ink-bright)" stroke-width="1.2"/></svg></div>
    <div class="social" style="left:191px; top:52px;"><div class="social__name">Picturo</div><svg class="social__mark" width="11" height="11" aria-hidden="true"><circle cx="5.5" cy="5.5" r="4.5" fill="none" stroke="var(--ink-bright)" stroke-width="1.2"/></svg></div>
    <div class="social" style="left:73px; top:103px;"><div class="social__name">Linkwork</div><svg class="social__mark" width="11" height="11" aria-hidden="true"><circle cx="5.5" cy="5.5" r="4.5" fill="none" stroke="var(--ink-bright)" stroke-width="1.2"/></svg></div>
    <div class="social" style="left:162px; top:103px;"><div class="social__name">Viewcast</div><svg class="social__mark" width="11" height="11" aria-hidden="true"><circle cx="5.5" cy="5.5" r="4.5" fill="none" stroke="var(--ink-bright)" stroke-width="1.2"/></svg></div>
  </div>

  <p class="legal" style="left:0; width:100%; text-align:center; top:1085px;">Copyright © 2020. Company Name All Right Reserved</p>
</footer>

</body>
</html>
```